International Digital Platform Startup needs powerpoint design

We need a powerpoint design for a new SaaS and platform startup based in Helsinki, Finland called Kelmori Ltd. We help companies to create, calculate and communicate customer value and capture that value into cashflow. Company owners, boards and management teams will use this platform and the digital tool to have a transparent customer value view. The digital tool helps everyone in the organisation to see how they can create value in their job.
Benefits of Beacons7ClientWorth - tool:
Emotional benefits:
- Helps me succeed
- I’m forerunner
- I’m up to date
- I accomplish
- process is under control
- Ease to lead
- Ease in communication

Rational benefits:
- Simplicity in complex world of value
- Clarity
- Easy access - low deployment threshold

The final design should express Kelmori's brand personality: Creative, Analytic, Curious, Trustworthy, Brave. Our color is green as seen in logos.
Updates

Hi, Thank you for everyone participating so far to design the powerpoint template for Kelmori. There are some essential emphasis I would like to point out to help you design for us: - Kelmori is the company name, and we are building the tool and the platform called Beacons7ClientWorth. The emphasis is on the Beacons7ClientWorth -logo thought the company name and logo Kelmori needs to be there. This is one of the most important parts of the design – it needs to work. Logos should also not been framed in anyway. - We don’t need that many different pages, but the ones that can be used for several purposes – Keep it simple. - Since we are a Finnish startup, we like to look like one. Visually that means highlighting Finnish and startup, both meaning for us o Nordic clarity and simplicity o Freshness o Nordic design - The green color in our logos is the company color – in our coming website we are also using more fresh, lighter “mint“ like color and white headings with Barlow bold and regular fonts. Since this font doesn't appear in microsoft powerpoint, please use some of the fonts that do. (it seems I'm not able to place a screenshot of our webpage here. I'll be happy to provide one for you if it needed. The webpage is not public yet) I hope to hear from you soon. I'm in need to use the powerpoint in about one week : ) Creating Value with You, Ulla

Hi, Kelmori website has now been published at kelmori-example.com. In english site, there might still be something that needs to be fixed, but I'm sure it will help you to succeed with your design proposal. if there is any additional information you would need for this work, please let me know. I would be more than happy to provide it for you. Ulla

```html
<!DOCTYPE html>
<html lang="en">
<head>
<meta charset="utf-8">
<title>Kelmori Master Slide Presentation</title>
<link href="https://fonts.googleapis.com/css2?family=Montserrat:wght@400;500;600;700;800&display=swap" rel="stylesheet">
<style>
:root{
  --green:#2fc121;
  --green-dark:#22a317;
  --black:#0c0c0c;
  --ink:#222;
  --grey:#8a8a8a;
  --light:#e9e9e9;
  --bg:#ececec;
  --white:#fff;
}
*{box-sizing:border-box;margin:0;padding:0}
html,body{width:1200px;height:3424px;overflow:hidden}
body{background:var(--bg);font-family:"Montserrat",Arial,sans-serif;color:var(--ink);position:relative}
.slide{position:absolute;width:533px;height:299px;background:var(--white);overflow:hidden;box-shadow:0 6px 14px rgba(0,0,0,.18)}
.c1{left:44px}.c2{left:623px}
.abs{position:absolute}
.band{position:absolute;left:0;top:0}
.band-title{position:absolute;left:49px;top:14px;color:var(--white);font-size:16px;font-weight:700;letter-spacing:.3px}
.small{font-size:6px;line-height:1.7;color:#666}
.tiny{font-size:5px;line-height:1.6;color:#888}
.brand{font-weight:500;font-size:30px;letter-spacing:-.5px}
.photo{position:absolute}
.hex{position:absolute}
.green{color:var(--green)}
.node{position:absolute;width:36px;height:36px;border-radius:50%;background:#fff;border:5px solid var(--black);font-size:7px;font-weight:700;display:flex;align-items:center;justify-content:center;box-shadow:0 3px 6px rgba(0,0,0,.2)}
.node.grey{border-color:#ddd}.node.g{border-color:var(--green)}
.node.g span{background:var(--green);color:#fff;width:100%;height:100%;border-radius:50%;display:flex;align-items:center;justify-content:center}
.road-label{position:absolute;width:120px;text-align:center}
.road-label b{display:block;font-size:6.5px;color:var(--ink);margin-top:2px}
.vcard{position:absolute;top:114px;width:124px;height:160px;border-radius:18px;background:#fff;box-shadow:0 4px 12px rgba(0,0,0,.15);text-align:center;padding:46px 12px 0}
.vcard h4{font-size:10px;font-weight:700;margin-bottom:8px}
.vcard::before{content:"";position:absolute;left:8px;top:30px;bottom:20px;border-left:1px dashed #999}
.tcard{position:absolute;width:74px;background:#fff;box-shadow:0 3px 8px rgba(0,0,0,.18);text-align:left;padding:10px 8px 0}
.tcard .stars{color:#e53;font-size:8px;letter-spacing:1px;margin:6px 0 4px}
.tcard .foot{background:var(--black);color:#fff;font-size:7px;font-weight:700;padding:6px 8px;margin:0 -8px}
.bar{position:absolute;left:258px;width:226px}
.bar .lbl{font-size:7px;font-weight:600;color:#555}
.bar .pct{position:absolute;right:0;top:0;font-size:7px;color:#666}
.bar .track{height:5px;background:var(--light);border-radius:3px;margin-top:8px}
.bar .fill{height:5px;border-radius:3px;background:var(--green)}
.bar .fill.k{background:var(--black)}
.ring-txt{position:absolute;font-size:20px;font-weight:700;text-align:center;width:60px}
.member{position:absolute;top:96px;width:120px;text-align:center}
.member .pic{width:94px;height:94px;border-radius:50%;margin:0 auto 8px;border:5px solid var(--black)}
.member h5{font-size:8px;font-weight:700}
.member .pos{font-size:5.5px;letter-spacing:2px;font-weight:600;margin:3px 0 6px}
.li{position:absolute;display:flex;align-items:center;gap:12px;font-size:10px;font-weight:500;white-space:nowrap}
.li.muted{color:#aaa}
.pbox{position:absolute;height:30px;border-radius:4px;font-size:7px;font-weight:600;display:flex;align-items:center;justify-content:center;box-shadow:0 2px 5px rgba(0,0,0,.2);background:#fff}
.pbox.g{background:var(--green);color:#fff;height:66px}
.pbox.gr{background:#9b9b9b;color:#fff}
.pbox.k{background:var(--black);color:#fff}
.badge{position:absolute;width:72px;height:38px;border-radius:8px;background:#fff;box-shadow:0 3px 8px rgba(0,0,0,.15);display:flex;align-items:center;justify-content:center}
.badge i{display:block;width:46px;height:10px;border-radius:5px;background:#cfcfcf}
.swot{position:absolute;width:40px;height:40px;border-radius:50%;background:#fff;border:7px solid var(--green);font-size:13px;font-weight:600;display:flex;align-items:center;justify-content:center}
.swot-txt{position:absolute;width:170px}
.swot-txt b{font-size:6px;display:block;margin-bottom:2px}
.contact{position:absolute;left:58px;display:flex;align-items:center;gap:12px;color:#fff;font-size:7px}
.tool-name{position:absolute;left:420px;top:128px;font-size:14px;font-weight:500;line-height:1.05;color:#222;white-space:nowrap}
.tool-name span{display:block}
.tool-name span:last-child{border-bottom:2px solid var(--green);display:inline-block}
</style>
</head>
<body>

<section class="slide c1" style="top:37px">
  <div class="photo" role="img" aria-label="faded workspace photo with laptop" style="inset:0;background:linear-gradient(160deg,#f6f6f6,#dcdcdc)"></div>
  <svg class="band" width="533" height="100"><path d="M0 0H533V50Q533 70 490 70H90Q40 70 20 90L0 100Z" fill="#0c0c0c"/></svg>
  <div class="abs brand" style="left:0;width:533px;text-align:center;top:6px;color:#fff">Kelmori</div>
  <div class="abs tiny" style="width:533px;text-align:center;top:84px;letter-spacing:3px;color:#333">www.yourwebsite.com</div>
  <div class="abs" style="width:533px;text-align:center;top:138px;font-size:20px;font-weight:700;letter-spacing:.5px">KELMORI MASTER SLIDE PRESENTATION</div>
  <div class="abs" style="left:198px;top:202px;width:138px;height:16px;border-radius:8px;background:#fff;border:2px solid #222;font-size:6.5px;font-weight:600;text-align:center;line-height:12px">PRESENTER NAME</div>
  <div class="abs" style="width:533px;text-align:center;top:248px;font-size:8px;font-weight:700;color:var(--green)">2020</div>
</section>

<section class="slide c2" style="top:37px;background:var(--green)">
  <svg class="band" width="533" height="299"><path d="M0 0H120V299H0Z" fill="#0c0c0c"/><path d="M130 60Q140 0 200 0H120V299H115V120Q115 80 130 60Z" fill="#0c0c0c"/></svg>
  <div class="photo" role="img" aria-label="team stacking hands photo" style="left:38px;top:45px;width:154px;height:165px;border-radius:8px 8px 34px 8px;background:linear-gradient(135deg,#9a9a9a,#3a3a3a)"></div>
  <div class="abs" style="right:22px;top:50px;text-align:right;color:#fff;font-size:20px;font-weight:800;line-height:1.15">MASTER SLIDE<br>PRESENTATION</div>
  <div class="abs" style="right:22px;top:106px;color:#fff;font-size:7px;letter-spacing:3px;font-weight:600">SUBTITLE GOES HERE</div>
  <div class="abs brand" style="right:24px;top:222px;color:#0c0c0c;font-size:34px">Kelmori</div>
</section>

<section class="slide c1" style="top:375px">
  <svg class="band" width="533" height="120"><path d="M0 0H466Q466 48 426 48H70Q0 48 0 118Z" fill="var(--green)"/></svg>
  <h2 class="band-title">ABOUT US</h2>
  <svg class="abs" style="left:32px;top:94px" width="18" height="18" viewBox="0 0 18 18"><path d="M2 9L9 2L16 9V16H11V11H7V16H2Z" fill="#111"/></svg>
  <p class="abs small" style="left:32px;top:126px;width:200px;text-align:justify">Lorem ipsum dolor sit amet, consectetuer adipiscing elit, sed diam nonummy nibh euismod tincidunt ut laoreet dolore magna aliquam erat volutpat. Ut wisi enim ad minim veniam, quis nostrud exerci tation ullamcorper suscipit lobortis nisl ut aliquip ex ea commodo consequat. Duis autem vel eum iriure dolor in hendrerit in vulputate velit esse molestie consequat, vel illum dolore eu feugiat nulla facilisis at vero eros et accumsan et iusto odio dignissim qui blandit praesent luptatum zzril delenit augue duis dolore te feugait nulla facilisi.</p>
  <div class="photo" role="img" aria-label="desk with keyboard and notebook photo" style="left:263px;top:66px;width:270px;height:233px;border-radius:34px 0 0 0;background:linear-gradient(135deg,#f2f2f2,#cfcfcf)"></div>
  <div class="abs brand" style="right:14px;top:258px;font-size:24px;color:#111">Kelmori</div>
</section>

<section class="slide c2" style="top:375px">
  <svg class="band" width="533" height="120"><path d="M0 0H466Q466 48 426 48H70Q0 48 0 118Z" fill="var(--green)"/></svg>
  <h2 class="band-title">OUR ROADMAP</h2>
  <svg class="abs" style="left:40px;top:180px" width="460" height="4"><line x1="0" y1="2" x2="460" y2="2" stroke="#555" stroke-dasharray="2 2"/></svg>
  <div class="node grey" style="left:76px;top:163px">2018</div>
  <div class="node" style="left:182px;top:163px">2019</div>
  <div class="node g" style="left:288px;top:163px"><span>2020</span></div>
  <div class="node" style="left:394px;top:163px">2021</div>
  <div class="road-label tiny" style="left:34px;top:80px">sit amet, consectetuer adipiscing elit, sed diam nonummy nibh euismod tincidunt<b>LOREM IPSUM DOLOR</b></div>
  <div class="road-label tiny" style="left:246px;top:80px">sit amet, consectetuer adipiscing elit, sed diam nonummy nibh euismod tincidunt<b>LOREM IPSUM DOLOR</b></div>
  <div class="road-label tiny" style="left:140px;top:237px"><b style="margin:0 0 2px">LOREM IPSUM DOLOR</b>sit amet, consectetuer adipiscing elit, sed diam nonummy nibh euismod tincidunt</div>
  <div class="road-label tiny" style="left:352px;top:237px"><b style="margin:0 0 2px">LOREM IPSUM DOLOR</b>sit amet, consectetuer adipiscing elit, sed diam nonummy nibh euismod tincidunt</div>
</section>

<section class="slide c1" style="top:712px">
  <svg class="band" width="533" height="120"><path d="M0 0H466Q466 48 426 48H70Q0 48 0 118Z" fill="var(--green)"/></svg>
  <h2 class="band-title">OUR VISION, VALUE &amp; GOAL</h2>
  <div class="vcard" style="left:46px"><h4 class="green">Lorem ipsum</h4><p class="tiny">Lorem ipsum dolor sit amet, consectetuer adipiscing elit, sed diam nonummy nibh euismod tincidunt ut laoreet dolore magna aliquam erat volutpat.</p></div>
  <div class="vcard" style="left:204px"><h4>Lorem ipsum</h4><p class="tiny">Lorem ipsum dolor sit amet, consectetuer adipiscing elit, sed diam nonummy nibh euismod tincidunt ut laoreet dolore magna aliquam erat volutpat.</p></div>
  <div class="vcard" style="left:362px"><h4 style="color:#888">Lorem ipsum</h4><p class="tiny">Lorem ipsum dolor sit amet, consectetuer adipiscing elit, sed diam nonummy nibh euismod tincidunt ut laoreet dolore magna aliquam erat volutpat.</p></div>
  <svg class="hex" style="left:86px;top:88px" width="46" height="50" viewBox="0 0 46 50"><polygon points="23,1 45,13 45,37 23,49 1,37 1,13" fill="var(--green)"/><ellipse cx="23" cy="25" rx="10" ry="6" fill="none" stroke="#fff" stroke-width="2"/><circle cx="23" cy="25" r="3" fill="#fff"/></svg>
  <svg class="hex" style="left:244px;top:88px" width="46" height="50" viewBox="0 0 46 50"><polygon points="23,1 45,13 45,37 23,49 1,37 1,13" fill="#111"/><circle cx="23" cy="25" r="9" fill="none" stroke="#fff" stroke-width="2"/><circle cx="23" cy="25" r="3" fill="#fff"/></svg>
  <svg class="hex" style="left:402px;top:88px" width="46" height="50" viewBox="0 0 46 50"><polygon points="23,1 45,13 45,37 23,49 1,37 1,13" fill="#8a8a8a"/><circle cx="23" cy="25" r="8" fill="none" stroke="#fff" stroke-width="2"/><path d="M23 13V37M11 25H35" stroke="#fff" stroke-width="1.5"/></svg>
</section>

<section class="slide c2" style="top:712px">
  <svg class="band" width="533" height="299"><path d="M0 0H445Q445 48 405 48H150Q110 48 110 88V299H0Z" fill="var(--green)"/></svg>
  <div class="abs" style="left:42px;top:64px;width:114px;height:162px;background:#0c0c0c;border-radius:16px 0 16px 0;color:#fff;padding:16px 14px">
    <div style="font-size:20px;font-weight:700;line-height:1.2">Title<br>Slide</div>
    <div style="font-size:6px;margin:4px 0 18px">(Testimonials)</div>
    <div style="font-size:6px;font-weight:600;line-height:1.6">Lorem ipsum is simply dummy text of the printing and typesetting industry</div>
  </div>
  <svg class="abs" style="left:170px;top:80px" width="320" height="80"><circle cx="4" cy="4" r="4" fill="#333"/><circle cx="4" cy="30" r="4" fill="#333"/><circle cx="4" cy="56" r="4" fill="#333"/><path d="M8 4H300V22M8 30H218V50M8 56H130V76" stroke="#555" fill="none"/></svg>
  <div class="tcard" style="left:188px;top:155px"><p class="tiny">Lorem ipsum is simply dummy text of the printing and typesetting industry</p><div class="stars">★★★★★</div><div class="foot">Lorem Ipsum</div></div>
  <div class="tcard" style="left:298px;top:128px"><p class="tiny">Lorem ipsum is simply dummy text of the printing and typesetting industry</p><div class="stars">★★★★★</div><div class="foot">Lorem Ipsum</div></div>
  <div class="tcard" style="left:408px;top:102px"><p class="tiny">Lorem ipsum is simply dummy text of the printing and typesetting industry</p><div class="stars">★★★★★</div><div class="foot">Lorem Ipsum</div></div>
</section>

<section class="slide c1" style="top:1050px">
  <svg class="band" width="533" height="120"><path d="M0 0H466Q466 48 426 48H70Q0 48 0 118Z" fill="var(--green)"/></svg>
  <h2 class="band-title">INFOGRAPHIC</h2>
  <svg class="abs" style="left:32px;top:86px" width="80" height="80" viewBox="0 0 80 80"><circle cx="40" cy="40" r="33" fill="#fff" stroke="#eee" stroke-width="6"/><circle cx="40" cy="40" r="33" fill="none" stroke="var(--green)" stroke-width="6" stroke-dasharray="151 207" transform="rotate(-90 40 40)"/></svg>
  <div class="ring-txt green" style="left:42px;top:114px">73%</div>
  <svg class="abs" style="left:32px;top:178px" width="80" height="80" viewBox="0 0 80 80"><circle cx="40" cy="40" r="33" fill="#fff" stroke="#eee" stroke-width="6"/><circle cx="40" cy="40" r="33" fill="none" stroke="#111" stroke-width="6" stroke-dasharray="104 207" transform="rotate(-90 40 40)"/></svg>
  <div class="ring-txt" style="left:42px;top:206px">50%</div>
  <div class="abs" style="left:124px;top:102px;width:100px"><b class="green" style="font-size:7px">PROJECT 01</b><p class="tiny">Lorem ipsum is simply dummy text of the printing and typesetting industry</p></div>
  <div class="abs" style="left:124px;top:194px;width:100px"><b style="font-size:7px">PROJECT 02</b><p class="tiny">Lorem ipsum is simply dummy text of the printing and typesetting industry</p></div>
  <div class="bar" style="top:88px"><span class="lbl">PROJECT 03</span><span class="pct">32%</span><div class="track"><div class="fill" style="width:32%"></div></div></div>
  <div class="bar" style="top:123px"><span class="lbl">PROJECT 04</span><span class="pct">72%</span><div class="track"><div class="fill k" style="width:72%"></div></div></div>
  <div class="bar" style="top:159px"><span class="lbl">PROJECT 05</span><span class="pct">52%</span><div class="track"><div class="fill" style="width:52%"></div></div></div>
  <div class="bar" style="top:195px"><span class="lbl">PROJECT 06</span><span class="pct">12%</span><div class="track"><div class="fill k" style="width:12%"></div></div></div>
  <div class="bar" style="top:230px"><span class="lbl">PROJECT 07</span><span class="pct">60%</span><div class="track"><div class="fill" style="width:60%"></div></div></div>
</section>

<section class="slide c2" style="top:1050px;background:var(--green)">
  <div class="photo" role="img" aria-label="meeting at a laptop photo" style="left:0;top:0;width:533px;height:140px;background:linear-gradient(135deg,#d8d8d8,#555)"></div>
  <div class="abs brand" style="right:10px;top:18px;font-size:24px;color:#111">Kelmori</div>
  <div class="abs" style="left:119px;top:140px;width:414px;height:159px;background:#fff;border-radius:40px 0 0 0"></div>
  <div class="abs" style="left:20px;top:180px;color:#fff;font-size:16px;font-weight:700;line-height:1.1">OUR<br>MISSION</div>
  <p class="abs small" style="left:162px;top:168px;width:348px">Lorem ipsum dolor sit amet, consectetuer adipiscing elit, sed diam nonummy nibh euismod tincidunt ut laoreet dolore magna aliquam erat volutpat. Ut wisi enim ad minim veniam, quis nostrud exerci tation ullamcorper suscipit lobortis nisl ut aliquip ex ea commodo consequat. Duis autem vel eum iriure dolor in hendrerit in vulputate velit esse molestie consequat, vel illum dolore eu feugiat nulla facilisis at vero eros et accumsan et iusto odio dignissim qui blandit praesent luptatum zzril delenit augue duis dolore te feugait nulla facilisi.</p>
</section>

<section class="slide c1" style="top:1387px">
  <svg class="band" width="533" height="120"><path d="M0 0H466Q466 48 426 48H70Q0 48 0 118Z" fill="var(--green)"/></svg>
  <h2 class="band-title">OUR FOUNDERS</h2>
  <div class="photo" role="img" aria-label="portrait photo of the founder" style="left:42px;top:86px;width:116px;height:172px;background:linear-gradient(160deg,#cfcfcf,#3b3b3b)"></div>
  <div class="abs" style="left:178px;top:106px;font-size:13px;font-weight:700">NAME</div>
  <div class="abs" style="left:178px;top:124px;font-size:6px;letter-spacing:3px;font-weight:600">FOUNDER/CEO</div>
  <p class="abs small" style="left:178px;top:144px;width:310px;text-align:justify;color:#333">Lorem ipsum dolor sit amet, consectetuer adipiscing elit, sed diam nonummy nibh euismod tincidunt ut laoreet dolore magna aliquam erat volutpat. Ut wisi enim ad minim veniam, quis nostrud exerci tation ullamcorper suscipit lobortis nisl ut aliquip ex ea commodo consequat. Duis autem vel eum iriure dolor in hendrerit in vulputate velit esse molestie consequat, vel illum dolore eu feugiat nulla facilisis at vero eros et accumsan et iusto odio dignissim qui blandit praesent luptatum zzril delenit augue duis dolore te feugait nulla facilisi.</p>
</section>

<section class="slide c2" style="top:1387px">
  <svg class="band" width="533" height="299"><path d="M0 0H533V130Q533 100 490 100H70Q0 100 0 160Z" fill="var(--green)"/></svg>
  <div class="abs" style="width:533px;text-align:center;top:20px;color:#fff;font-size:16px;font-weight:700">OUR TEAM</div>
  <div class="abs" style="left:252px;top:48px;width:30px;border-top:2px solid #fff"></div>
  <div class="member" style="left:48px"><div class="pic" role="img" aria-label="team member portrait" style="background:linear-gradient(160deg,#d5d5d5,#555)"></div><h5>NAME</h5><div class="pos">POTITION</div><p class="tiny" style="color:#333">Lorem ipsum dolor sit amet, consectetuer adipiscing elit, sed diam nonummy nibh</p></div>
  <div class="member" style="left:206px"><div class="pic" role="img" aria-label="team member portrait" style="background:linear-gradient(160deg,#d5d5d5,#444)"></div><h5 class="green">NAME</h5><div class="pos green">POTITION</div><p class="tiny green">Lorem ipsum dolor sit amet, consectetuer adipiscing elit, sed diam nonummy nibh</p></div>
  <div class="member" style="left:356px"><div class="pic" role="img" aria-label="team member portrait" style="background:linear-gradient(160deg,#e0e0e0,#666)"></div><h5 style="color:#888">NAME</h5><div class="pos" style="color:#888">POTITION</div><p class="tiny">Lorem ipsum dolor sit amet, consectetuer adipiscing elit, sed diam nonummy nibh</p></div>
</section>

<section class="slide c1" style="top:1725px">
  <svg class="abs" style="left:0;top:0" width="240" height="299"><path d="M0 0H110Q222 0 222 150Q222 299 110 299H0Z" fill="var(--green)"/></svg>
  <div class="photo" role="img" aria-label="people working in an office photo" style="left:0;top:0;width:205px;height:299px;border-radius:0 150px 150px 0;background:linear-gradient(135deg,#777,#2a2a2a)"></div>
  <div class="abs" style="left:16px;top:122px;color:#fff;font-size:17px;font-weight:700;line-height:1.2">SaaS<br>PROJECTS</div>
  <svg class="abs" style="left:18px;top:180px" width="20" height="20"><circle cx="7" cy="8" r="6" fill="none" stroke="#fff"/><circle cx="13" cy="8" r="6" fill="none" stroke="#fff"/><circle cx="10" cy="13" r="6" fill="none" stroke="#fff"/></svg>
  <svg class="abs" style="left:260px;top:8px" width="80" height="280"><path d="M6 2Q70 20 40 60Q10 100 60 130Q100 160 40 200Q10 230 14 276" stroke="#888" fill="none" stroke-dasharray="2 3"/></svg>
  <svg class="hex" style="left:266px;top:20px" width="46" height="50" viewBox="0 0 46 50"><polygon points="23,1 45,13 45,37 23,49 1,37 1,13" fill="#111" stroke="#ddd" stroke-width="2"/><path d="M14 22L23 17L32 22L23 27Z M14 28L23 33L32 28" fill="none" stroke="#fff" stroke-width="1.6"/></svg>
  <svg class="hex" style="left:296px;top:88px" width="46" height="50" viewBox="0 0 46 50"><polygon points="23,1 45,13 45,37 23,49 1,37 1,13" fill="#111" stroke="#ddd" stroke-width="2"/><rect x="15" y="16" width="16" height="18" rx="2" fill="none" stroke="#fff" stroke-width="1.6"/></svg>
  <svg class="hex" style="left:296px;top:156px" width="46" height="50" viewBox="0 0 46 50"><polygon points="23,1 45,13 45,37 23,49 1,37 1,13" fill="#8a8a8a" stroke="#ddd" stroke-width="2"/><rect x="14" y="18" width="18" height="14" fill="none" stroke="#fff" stroke-width="1.6"/></svg>
  <svg class="hex" style="left:266px;top:224px" width="46" height="50" viewBox="0 0 46 50"><polygon points="23,1 45,13 45,37 23,49 1,37 1,13" fill="#111" stroke="#ddd" stroke-width="2"/><circle cx="23" cy="25" r="8" fill="none" stroke="#fff" stroke-width="1.6"/></svg>
  <div class="abs" style="left:332px;top:30px;width:130px"><b style="font-size:9px;font-weight:500">Lorem ipsum</b><p class="tiny">Lorem ipsum dolor sit amet, consectetuer adipiscing elit.</p></div>
  <div class="abs" style="left:362px;top:98px;width:130px"><b style="font-size:9px;font-weight:500">Lorem ipsum</b><p class="tiny">Lorem ipsum dolor sit amet, consectetuer adipiscing elit.</p></div>
  <div class="abs" style="left:362px;top:166px;width:130px"><b style="font-size:9px;font-weight:500">Lorem ipsum</b><p class="tiny">Lorem ipsum dolor sit amet, consectetuer adipiscing elit.</p></div>
  <div class="abs" style="left:338px;top:234px;width:130px"><b style="font-size:9px;font-weight:500">Lorem ipsum</b><p class="tiny">Lorem ipsum dolor sit amet, consectetuer adipiscing elit.</p></div>
</section>

<section class="slide c2" style="top:1725px">
  <svg class="abs" style="left:380px;top:0" width="153" height="299"><path d="M0 0H153V299H20V60Q20 0 0 0Z" fill="var(--green)"/><rect x="10" y="40" width="8" height="259" fill="#0c0c0c"/></svg>
  <div class="abs" style="left:380px;top:0;width:153px;height:299px;background:#fff;clip-path:polygon(0 0,40% 0,30% 100%,0 100%)"></div>
  <div class="photo" role="img" aria-label="overhead photo of laptops on a desk" style="left:348px;top:52px;width:150px;height:210px;border-radius:30px 8px 30px 8px;background:linear-gradient(135deg,#888,#222);box-shadow:0 4px 10px rgba(0,0,0,.3)"></div>
  <div class="abs" style="left:40px;top:56px;font-size:18px;font-weight:700">PROJECT 01</div>
  <div class="abs" style="left:40px;top:84px;font-size:6px;letter-spacing:3px;font-weight:600;color:#666">SUBTITLE GOES HERE</div>
  <p class="abs small" style="left:40px;top:116px;width:262px;text-align:justify">Lorem ipsum dolor sit amet, consectetuer adipiscing elit, sed diam nonummy nibh euismod tincidunt ut laoreet dolore magna aliquam erat volutpat. Ut wisi enim ad minim veniam, quis nostrud exerci tation ullamcorper suscipit lobortis nisl ut aliquip ex ea commodo consequat. Duis autem vel eum iriure dolor in hendrerit in vulputate velit esse molestie consequat, vel illum dolore eu feugiat nulla facilisis at vero eros et accumsan et iusto odio dignissim qui blandit praesent luptatum zzril delenit augue duis dolore te feugait nulla facilisi.</p>
</section>

<section class="slide c1" style="top:2063px">
  <div class="abs" style="width:533px;text-align:center;top:12px;font-size:15px;font-weight:700">OUR PLATFORM</div>
  <div class="abs" style="left:250px;top:34px;width:34px;border-top:2px solid var(--green)"></div>
  <div class="abs" style="left:46px;top:52px;width:442px;height:232px;border:1px dashed #999;border-radius:16px"></div>
  <div class="abs" style="left:110px;top:60px;width:312px;height:58px;background:#fff;border-radius:8px;box-shadow:0 3px 10px rgba(0,0,0,.18);display:flex;align-items:center;justify-content:center"><span class="brand" style="font-size:28px;color:#111">Kelmori</span></div>
  <svg class="abs" style="left:0;top:0" width="533" height="299"><path d="M196 130V170H166M196 130V240H166M330 124V150H364M336 124V186H364M342 124V222H364M348 124V258H364" stroke="var(--green)" fill="none" stroke-dasharray="2 2"/><path d="M240 125V280" stroke="#999" fill="none" stroke-dasharray="2 2"/></svg>
  <div class="pbox g" style="left:64px;top:130px;width:100px">Lorem ipsum</div>
  <div class="pbox g" style="left:64px;top:202px;width:100px">Lorem ipsum</div>
  <div class="pbox" style="left:216px;top:133px;width:104px">Lorem ipsum</div>
  <div class="pbox" style="left:216px;top:169px;width:104px">Lorem ipsum</div>
  <div class="pbox" style="left:216px;top:205px;width:104px">Lorem ipsum</div>
  <div class="pbox" style="left:216px;top:241px;width:104px">Lorem ipsum</div>
  <div class="pbox gr" style="left:364px;top:133px;width:104px">Lorem ipsum</div>
  <div class="pbox gr" style="left:364px;top:169px;width:104px">Lorem ipsum</div>
  <div class="pbox k" style="left:364px;top:205px;width:104px">Lorem ipsum</div>
  <div class="pbox gr" style="left:364px;top:241px;width:104px">Lorem ipsum</div>
</section>

<section class="slide c2" style="top:2063px">
  <div class="photo" role="img" aria-label="dark photo of a laptop on a wooden table" style="inset:0;background:linear-gradient(135deg,#6a6a6a,#1e1e1e)"></div>
  <div class="abs" style="left:64px;top:44px;width:312px;height:208px;border:1px solid rgba(255,255,255,.8);border-radius:22px 0 22px 0"></div>
  <div class="abs" style="left:46px;top:78px;width:274px;height:186px;background:rgba(47,193,33,.88);border-radius:20px 0 20px 0"></div>
  <div class="abs brand" style="left:224px;top:82px;color:#111;font-size:30px">Kelmori</div>
  <div class="abs" style="left:78px;top:196px;color:#fff;font-size:18px;font-weight:700">SECTION BREAK</div>
  <div class="abs" style="left:78px;top:226px;width:46px;border-top:2px solid #fff"></div>
</section>

<section class="slide c1" style="top:2400px">
  <svg class="band" width="533" height="120"><path d="M0 0H466Q466 48 426 48H70Q0 48 0 118Z" fill="var(--green)"/></svg>
  <h2 class="band-title" style="left:40px">OUR PARTNERS</h2>
  <div class="badge" style="left:86px;top:102px"><i></i></div>
  <div class="badge" style="left:182px;top:102px"><i></i></div>
  <div class="badge" style="left:278px;top:102px"><i></i></div>
  <div class="badge" style="left:374px;top:102px"><i></i></div>
  <div class="badge" style="left:86px;top:154px"><i></i></div>
  <div class="badge" style="left:182px;top:154px"><i></i></div>
  <div class="badge" style="left:278px;top:154px"><i></i></div>
  <div class="badge" style="left:374px;top:154px"><i></i></div>
  <div class="badge" style="left:86px;top:206px"><i></i></div>
  <div class="badge" style="left:182px;top:206px"><i style="width:18px;height:18px;border-radius:50%"></i></div>
  <div class="badge" style="left:278px;top:206px"><i></i></div>
  <div class="badge" style="left:374px;top:206px"><i style="width:18px;height:18px;border-radius:50%"></i></div>
</section>

<section class="slide c2" style="top:2400px">
  <svg class="band" width="533" height="120"><path d="M0 0H466Q466 48 426 48H70Q0 48 0 118Z" fill="var(--green)"/></svg>
  <h2 class="band-title">OUR ANALYSIS</h2>
  <svg class="abs" style="left:214px;top:126px" width="106" height="106"><path d="M53 53L18 18M53 53L88 18M53 53L18 88M53 53L88 88" stroke="#0c0c0c" stroke-width="34"/><circle cx="53" cy="53" r="24" fill="#0c0c0c"/></svg>
  <div class="abs" style="left:246px;top:173px;font-size:7px;color:#fff;font-weight:500">Kelmori</div>
  <div class="swot" style="left:247px;top:106px">S</div>
  <div class="swot" style="left:207px;top:146px">T</div>
  <div class="swot" style="left:287px;top:146px">W</div>
  <div class="swot" style="left:247px;top:186px">O</div>
  <div class="swot-txt tiny" style="left:18px;top:98px;text-align:right"><b style="color:#222">STRENGTH</b>Lorem ipsum dolor sit amet, consectetuer adipiscing elit, sed diam nonummy nibh euismod tincidunt ut laoreet dolore magna aliquam erat</div>
  <div class="swot-txt tiny" style="left:346px;top:98px"><b style="color:#222">WEAKNESS</b>Lorem ipsum dolor sit amet, consectetuer adipiscing elit, sed diam nonummy nibh euismod tincidunt ut laoreet dolore magna aliquam erat</div>
  <div class="swot-txt tiny" style="left:18px;top:208px;text-align:right"><b style="color:#222">THREAT</b>Lorem ipsum dolor sit amet, consectetuer adipiscing elit, sed diam nonummy nibh euismod tincidunt ut laoreet dolore magna aliquam erat</div>
  <div class="swot-txt tiny" style="left:346px;top:208px"><b style="color:#222">OPPORTUNITY</b>Lorem ipsum dolor sit amet, consectetuer adipiscing elit, sed diam nonummy nibh euismod tincidunt ut laoreet dolore magna aliquam erat</div>
</section>

<section class="slide c1" style="top:2738px">
  <svg class="band" width="533" height="120"><path d="M0 0H466Q466 48 426 48H70Q0 48 0 118Z" fill="var(--green)"/></svg>
  <h2 class="band-title">EMOTIONAL BENEFITS</h2>
  <div class="li" style="left:64px;top:92px"><svg width="30" height="32" viewBox="0 0 46 50"><polygon points="23,1 45,13 45,37 23,49 1,37 1,13" fill="#111" stroke="#ddd" stroke-width="3"/><circle cx="23" cy="25" r="8" fill="none" stroke="#fff" stroke-width="2.5"/></svg>Helps me succeed</div>
  <div class="li" style="left:64px;top:132px"><svg width="30" height="32" viewBox="0 0 46 50"><polygon points="23,1 45,13 45,37 23,49 1,37 1,13" fill="#111" stroke="#ddd" stroke-width="3"/><circle cx="23" cy="25" r="8" fill="none" stroke="#fff" stroke-width="2.5"/><path d="M23 20V25H27" stroke="#fff" stroke-width="2"/></svg>I’m forerunner</div>
  <div class="li" style="left:64px;top:172px"><svg width="30" height="32" viewBox="0 0 46 50"><polygon points="23,1 45,13 45,37 23,49 1,37 1,13" fill="#111" stroke="#ddd" stroke-width="3"/><rect x="15" y="17" width="16" height="16" fill="none" stroke="#fff" stroke-width="2.5"/></svg>I’m up to date</div>
  <div class="li" style="left:64px;top:212px"><svg width="30" height="32" viewBox="0 0 46 50"><polygon points="23,1 45,13 45,37 23,49 1,37 1,13" fill="#111" stroke="#ddd" stroke-width="3"/><path d="M16 25L21 30L31 19" fill="none" stroke="#fff" stroke-width="2.5"/></svg>I accomplish</div>
  <div class="li" style="left:278px;top:92px"><svg width="30" height="32" viewBox="0 0 46 50"><polygon points="23,1 45,13 45,37 23,49 1,37 1,13" fill="#111" stroke="#ddd" stroke-width="3"/><circle cx="23" cy="25" r="8" fill="none" stroke="#fff" stroke-width="2.5"/></svg>process is under control</div>
  <div class="li" style="left:278px;top:132px"><svg width="30" height="32" viewBox="0 0 46 50"><polygon points="23,1 45,13 45,37 23,49 1,37 1,13" fill="#111" stroke="#ddd" stroke-width="3"/><rect x="15" y="17" width="16" height="16" fill="none" stroke="#fff" stroke-width="2.5"/></svg>Ease to lead</div>
  <div class="li" style="left:278px;top:172px"><svg width="30" height="32" viewBox="0 0 46 50"><polygon points="23,1 45,13 45,37 23,49 1,37 1,13" fill="#111" stroke="#ddd" stroke-width="3"/><path d="M15 18H31L15 32H31Z" fill="none" stroke="#fff" stroke-width="2.5"/></svg>Ease in communication</div>
  <div class="li muted" style="left:278px;top:212px"><svg width="30" height="32" viewBox="0 0 46 50"><polygon points="23,1 45,13 45,37 23,49 1,37 1,13" fill="var(--green)" stroke="#ddd" stroke-width="3"/></svg>Add another benefit here</div>
</section>

<section class="slide c2" style="top:2738px">
  <svg class="band" width="533" height="120"><path d="M0 0H466Q466 48 426 48H70Q0 48 0 118Z" fill="var(--green)"/></svg>
  <h2 class="band-title">RATIONAL BENEFITS</h2>
  <div class="li" style="left:72px;top:92px"><svg width="30" height="32" viewBox="0 0 46 50"><polygon points="23,1 45,13 45,37 23,49 1,37 1,13" fill="#111" stroke="#ddd" stroke-width="3"/><circle cx="23" cy="23" r="7" fill="none" stroke="#fff" stroke-width="2.5"/><path d="M20 32H26" stroke="#fff" stroke-width="2.5"/></svg>Simplicity in complex world of value</div>
  <div class="li" style="left:72px;top:132px"><svg width="30" height="32" viewBox="0 0 46 50"><polygon points="23,1 45,13 45,37 23,49 1,37 1,13" fill="#111" stroke="#ddd" stroke-width="3"/><circle cx="23" cy="25" r="8" fill="none" stroke="#fff" stroke-width="2.5"/></svg>Clarity</div>
  <div class="li" style="left:72px;top:172px"><svg width="30" height="32" viewBox="0 0 46 50"><polygon points="23,1 45,13 45,37 23,49 1,37 1,13" fill="#111" stroke="#ddd" stroke-width="3"/><path d="M16 33V27M21 33V22M26 33V25M31 33V18" stroke="#fff" stroke-width="2.5"/></svg>Easy access - low deployment threshold</div>
  <div class="li muted" style="left:72px;top:212px"><svg width="30" height="32" viewBox="0 0 46 50"><polygon points="23,1 45,13 45,37 23,49 1,37 1,13" fill="var(--green)" stroke="#ddd" stroke-width="3"/></svg>Add another benefit here</div>
  <div class="tool-name" aria-label="Beacons7ClientWorth"><span>Beacons7</span><span>Client</span><span>Worth</span></div>
</section>

<section class="slide c1" style="top:3076px">
  <div class="abs" style="width:533px;text-align:center;top:18px;font-size:13px;font-weight:700">FREE EDITABLE VECTOR ICON LINKS AVAILABLE</div>
  <div class="photo" role="img" aria-label="grid of editable line icons" style="left:26px;top:64px;width:480px;height:212px;background:linear-gradient(180deg,#e2e2e2,#d4d4d4);border-radius:4px"></div>
</section>

<section class="slide c2" style="top:3076px">
  <svg class="band" width="533" height="299"><path d="M533 20V70Q533 40 505 40Q533 30 533 20Z" fill="var(--green)"/><path d="M0 299V150Q0 120 40 120H460Q533 120 533 60V299Z" fill="var(--green)"/></svg>
  <div class="abs" style="left:52px;top:38px;font-size:20px;font-weight:700">THANK YOU</div>
  <div class="abs" style="left:52px;top:72px;width:54px;border-top:3px solid #111"></div>
  <div class="photo" role="img" aria-label="portrait photo of the presenter" style="left:340px;top:76px;width:112px;height:112px;border-radius:50%;border:5px solid #fff;background:linear-gradient(160deg,#d0d0d0,#4a4a4a)"></div>
  <div class="abs" style="left:40px;top:160px;color:#fff;font-size:10px;font-weight:700">PRESENTER NAME</div>
  <div class="contact" style="left:42px;top:180px"><svg width="10" height="10" viewBox="0 0 10 10"><path d="M2 1L4 3L3 4Q4 6 6 7L7 6L9 8L8 9Q2 9 1 2Z" fill="#fff"/></svg>+1 234 567 890</div>
  <div class="contact" style="left:42px;top:203px"><svg width="10" height="10"><circle cx="5" cy="5" r="4" fill="none" stroke="#fff"/><path d="M1 5H9M5 1V9" stroke="#fff"/></svg>www.yourwebsite.com</div>
  <div class="contact" style="left:42px;top:226px"><svg width="10" height="10"><rect x="1" y="2" width="8" height="6" fill="none" stroke="#fff"/><path d="M1 2L5 6L9 2" stroke="#fff" fill="none"/></svg>addyouremail@here.com</div>
  <div class="contact" style="left:42px;top:249px"><svg width="10" height="10"><path d="M5 9Q1 5 1 4A4 4 0 0 1 9 4Q9 5 5 9Z" fill="#fff"/></svg>Add your location here</div>
  <div class="abs brand" style="left:344px;top:240px;color:#111;font-size:30px">Kelmori</div>
</section>

</body>
</html>
```